Verbena Home- Hang tags for Modern Handmade Home Decor products

We need to design some hang tags to use for our products, we want double tags, meaning two tags that go together on one string, two different and coordinating sizes and shapes. We have a logo, what we need is the artwork for these two tags to take to print. One tag will have the logo on one side and company information on the other, the second tag will be for product information. For example, we specialize in handmade pieces from Latin America, on the product tag I want space to write the product info but also a line for what country it's from and what community created it. I'm attaching an image of the shapes of tags that I like, along with a copy of our logo. On the larger company tag I'd like our logo in the center and a color block stripe of the yellow color of our logo at the bottom, on the flip side there will just be text, sort of our company motto. On the narrower longer product info tag I'd like a small logo at the bottom end and space for product information to be written in by hand and on the flip side of this one lines for what country it's from, what community created it and care instructions, again, all information that we will write in by hand. Please let me know if you have questions.

Target Market(s)

Design savvy, house proud, well educated people who travel and appreciate art.

Font styles to use
Sans Serif

Requirements
Must have
• I want it to look graphic, sophisticated and modern. I want to be very legible and clean.
Nice to have
• Clarity, easy to read, and maybe a bit of whimsy or lightheartedness.
Should not have
• Nothing that feels "ethnic" or "crafty:, even though our products are handmade in Latin America they are contemporary and sophisticated, not stereotypical.

```html
<!DOCTYPE html>
<html lang="en">
<head>
<meta charset="utf-8">
<title>Verbena Home – Hang Tags</title>
<link rel="stylesheet" href="https://fonts.googleapis.com/css2?family=Quicksand:wght@400;500&display=swap">
<style>
  :root {
    --page: #f4f4f2;
    --kraft: #d3b47d;
    --paper: #ffffff;
    --paper-edge: #e3e3e0;
    --ink: #2f2d2c;
    --yellow: #f6c81c;
  }
  * { margin: 0; padding: 0; box-sizing: border-box; }
  html, body {
    width: 1200px;
    height: 1113px;
    overflow: hidden;
    background: var(--page);
    font-family: "Quicksand", sans-serif;
    color: var(--ink);
  }
  .canvas { position: relative; width: 1200px; height: 1113px; }

  .tag { position: absolute; }
  .tag-hole {
    position: absolute;
    top: 22px;
    left: 50%;
    width: 18px;
    height: 18px;
    margin-left: -9px;
    border-radius: 50%;
    background: var(--page);
  }

  /* Company tag (kraft) */
  .company-tag {
    width: 205px;
    height: 333px;
    background: var(--kraft);
    clip-path: polygon(22px 0, 183px 0, 205px 28px, 205px 333px, 0 333px, 0 28px);
  }
  .company-tag .stripe {
    position: absolute;
    left: 0; right: 0; bottom: 0;
    height: 19px;
    background: var(--yellow);
  }
  .company-tag .brand {
    position: absolute;
    top: 198px;
    left: 0; right: 0;
    text-align: center;
  }
  .brand-name {
    display: block;
    font-size: 30px;
    font-weight: 400;
    letter-spacing: 0.5px;
    line-height: 1;
  }
  .brand-url {
    display: block;
    margin-top: 6px;
    font-size: 7px;
    letter-spacing: 1.6px;
  }
  .company-tag .motto {
    position: absolute;
    top: 72px;
    left: 22px; right: 22px;
    text-align: center;
    font-size: 12px;
    line-height: 19px;
  }

  /* Product tag (white, long) */
  .product-tag {
    width: 210px;
    height: 565px;
    background: var(--paper);
    border: 1px solid var(--paper-edge);
  }
  .product-tag .origin-note {
    position: absolute;
    top: 70px;
    left: 0; right: 0;
    text-align: center;
    font-size: 12px;
    line-height: 17px;
  }
  .product-tag .field-label {
    position: absolute;
    left: 22px;
    font-size: 12px;
  }
  .product-tag .brand {
    position: absolute;
    bottom: 38px;
    left: 0; right: 0;
    text-align: center;
  }
  .product-tag .brand-name { font-size: 28px; }
  .product-tag .stripe {
    position: absolute;
    left: 0; right: 0; bottom: 0;
    height: 16px;
    background: var(--yellow);
  }
  .product-tag .write-in {
    position: absolute;
    top: 80px;
    left: 18px; right: 18px;
    height: 330px;
    border: 1px solid var(--ink);
  }
  .product-tag .write-in .divider {
    position: absolute;
    left: 0; right: 0;
    top: 145px;
    border-top: 1px solid var(--ink);
  }
</style>
</head>
<body>
<main class="canvas">

  <!-- Front side pair -->
  <section class="tag company-tag" style="left:105px; top:220px;">
    <span class="tag-hole"></span>
    <div class="brand">
      <span class="brand-name">verbena</span>
      <span class="brand-url">www.verbenahome.com</span>
    </div>
    <span class="stripe"></span>
  </section>

  <section class="tag product-tag" style="left:335px; top:220px;">
    <span class="tag-hole"></span>
    <p class="origin-note">Handmade<br>in Latin America</p>
    <p class="field-label" style="top:130px;">Product information:</p>
    <div class="brand">
      <span class="brand-name">verbena</span>
      <span class="brand-url">www.verbenahome.com</span>
    </div>
    <span class="stripe"></span>
  </section>

  <!-- Back side pair -->
  <section class="tag company-tag" style="left:655px; top:220px;">
    <span class="tag-hole"></span>
    <p class="motto">Verbena Home is a home décor studio co-creating beautiful and unique handmade pieces with artisan partners throughout Latin America, made by hand and heart and designed for the modern home.</p>
  </section>

  <section class="tag product-tag" style="left:885px; top:220px;">
    <span class="tag-hole"></span>
    <div class="write-in"><span class="divider"></span></div>
    <p class="field-label" style="top:432px;">Care instructions :</p>
  </section>

</main>
</body>
</html>
```